IT CEO and Real Estate Investor

It should include two roles and be a two sided card (both roles can be one a single side with a creative view or on different sides).
Card must be creative and interesting, but still professional.
Phone countries(USA/Russia) might be as flags or words, whatever works better.
Boris Melnovetz
Skype: boris_m
E-mail: melnovetz@quorbamail.com
Facebook: plavbook.example/melnovetz
Linkedin: trelnet.example/in/melnovetz
Phone (US): 1(555)316-2947
Phone (RUS): 7(955)482-3170
First role:
Pex Lattor (pexlattor.example) - include logo or part of logo (the $)
E-Commerce Automation Solutions
Founder/CEO/CTO
Second role:
Real Estate Investor
Cleveland, OH
UPDATE:
Let's do one side as logo only and all information on the other side - I don't like designs with information on both sides.
I also really liked designs on black (or other dark) background

```html
<!DOCTYPE html>
<html lang="en">
<head>
<meta charset="utf-8">
<title>Pex Lattor – Business Card</title>
<link rel="stylesheet" href="https://fonts.googleapis.com/css2?family=Montserrat:wght@500&family=Roboto:wght@400;500&display=swap">
<style>
  :root {
    --stage: #3a2a22;
    --card-dark: #141414;
    --card-light: #ffffff;
    --brand-blue: #29a8e0;
    --text-grey: #7d7d7d;
    --rule-grey: #c4c4c4;
    --label: #ffffff;
  }
  * { margin: 0; padding: 0; box-sizing: border-box; }
  html, body {
    width: 1200px; height: 1000px; overflow: hidden;
    background: var(--stage);
    font-family: "Roboto", Arial, sans-serif;
  }
  .canvas { position: relative; width: 1200px; height: 1000px; }

  .card {
    position: absolute; left: 351px; width: 498px; height: 284px;
    box-shadow: 0 2px 8px rgba(0,0,0,.35);
  }
  .card--front { top: 53px; background: var(--card-dark); }
  .card--back-1 { top: 353px; background: var(--card-light); }
  .card--back-2 { top: 662px; background: var(--card-light); }

  .side-label {
    position: absolute; left: 914px; color: var(--label);
    font-size: 24px; font-weight: 400;
  }

  .brand {
    position: absolute; display: flex; align-items: center;
    font-family: "Montserrat", Arial, sans-serif; font-weight: 500;
    color: var(--brand-blue); letter-spacing: 2px; white-space: nowrap;
  }
  .brand__mark { background: var(--brand-blue); flex: none; }
  .card--front .brand { left: 96px; top: 122px; font-size: 34px; gap: 16px; }
  .card--front .brand__mark { width: 40px; height: 40px; }
  .card--back-1 .brand, .card--back-2 .brand { left: 38px; top: 128px; font-size: 21px; gap: 10px; }
  .card--back-1 .brand__mark, .card--back-2 .brand__mark { width: 24px; height: 24px; }

  .divider {
    position: absolute; left: 248px; top: 72px; width: 1px; height: 142px;
    background: linear-gradient(to bottom, transparent, #b8b8b8 20%, #b8b8b8 80%, transparent);
  }

  .details { position: absolute; left: 268px; top: 66px; color: var(--text-grey); font-size: 11px; line-height: 14px; }
  .details__name { color: var(--brand-blue); font-size: 15px; font-weight: 500; line-height: 18px; }
  .details__role { margin-bottom: 12px; }
  .contact { display: flex; align-items: center; gap: 5px; line-height: 16px; }
  .contact svg { flex: none; }
  .social { display: flex; align-items: center; gap: 4px; margin-top: 12px; }
  .social__box { width: 11px; height: 11px; border: 1px solid var(--brand-blue); border-radius: 2px; }
  .social__handle { margin-left: 4px; }

  .base-rule { position: absolute; left: 0; width: 100%; }
  .base-rule--grey { top: 266px; height: 5px; background: var(--rule-grey); }
  .base-rule--blue { top: 275px; height: 9px; background: var(--brand-blue); }
</style>
</head>
<body>
<main class="canvas">

  <section class="card card--front" aria-label="Card front">
    <div class="brand"><span class="brand__mark"></span>PEX LATTOR</div>
  </section>
  <span class="side-label" style="top:190px">Front</span>

  <section class="card card--back-1" aria-label="Card back, technology role">
    <div class="brand"><span class="brand__mark"></span>PEX LATTOR</div>
    <div class="divider"></div>
    <div class="details">
      <p class="details__name">Boris Melnovetz</p>
      <p>E-Commerce Automation Solutions</p>
      <p class="details__role">Founder/CEO/CTO</p>
      <p class="contact">
        <svg width="8" height="8" viewBox="0 0 10 10"><path d="M2 0l2 2.5-1.2 1.3a6 6 0 003.4 3.4L7.5 6 10 8 8.5 10C4 10 0 6 0 1.5z" fill="#29a8e0"/></svg>
        1(555)316-2947
        <svg width="12" height="8" viewBox="0 0 12 8"><rect width="12" height="8" fill="#b22234"/><rect y="1.2" width="12" height="1.1" fill="#fff"/><rect y="3.4" width="12" height="1.1" fill="#fff"/><rect y="5.6" width="12" height="1.1" fill="#fff"/><rect width="5" height="4.5" fill="#3c3b6e"/></svg>
      </p>
      <p class="contact">
        <svg width="8" height="8" viewBox="0 0 10 10"><path d="M2 0l2 2.5-1.2 1.3a6 6 0 003.4 3.4L7.5 6 10 8 8.5 10C4 10 0 6 0 1.5z" fill="#29a8e0"/></svg>
        7(955)482-3170
        <svg width="12" height="8" viewBox="0 0 12 8"><rect width="12" height="2.7" fill="#fff" stroke="#ddd" stroke-width=".3"/><rect y="2.7" width="12" height="2.7" fill="#0039a6"/><rect y="5.3" width="12" height="2.7" fill="#d52b1e"/></svg>
      </p>
      <p class="contact">
        <svg width="8" height="6" viewBox="0 0 10 7"><rect width="10" height="7" fill="#29a8e0"/><path d="M0 0l5 4 5-4" stroke="#fff" fill="none"/></svg>
        melnovetz@quorbamail.com
      </p>
      <p class="contact">
        <svg width="8" height="8" viewBox="0 0 10 10"><circle cx="5" cy="5" r="5" fill="#29a8e0"/></svg>
        boris_m
      </p>
      <p class="social"><span class="social__box"></span><span class="social__box"></span><span class="social__handle">/melnovetz</span></p>
    </div>
    <div class="base-rule base-rule--grey"></div>
    <div class="base-rule base-rule--blue"></div>
  </section>
  <span class="side-label" style="top:495px">Back 1</span>

  <section class="card card--back-2" aria-label="Card back, investor role">
    <div class="brand"><span class="brand__mark"></span>PEX LATTOR</div>
    <div class="divider"></div>
    <div class="details">
      <p class="details__name">Boris Melnovetz</p>
      <p>Real Estate Investor</p>
      <p class="details__role">Cleveland, OH</p>
      <p class="contact">
        <svg width="8" height="8" viewBox="0 0 10 10"><path d="M2 0l2 2.5-1.2 1.3a6 6 0 003.4 3.4L7.5 6 10 8 8.5 10C4 10 0 6 0 1.5z" fill="#29a8e0"/></svg>
        1(555)316-2947
        <svg width="12" height="8" viewBox="0 0 12 8"><rect width="12" height="8" fill="#b22234"/><rect y="1.2" width="12" height="1.1" fill="#fff"/><rect y="3.4" width="12" height="1.1" fill="#fff"/><rect y="5.6" width="12" height="1.1" fill="#fff"/><rect width="5" height="4.5" fill="#3c3b6e"/></svg>
      </p>
      <p class="contact">
        <svg width="8" height="8" viewBox="0 0 10 10"><path d="M2 0l2 2.5-1.2 1.3a6 6 0 003.4 3.4L7.5 6 10 8 8.5 10C4 10 0 6 0 1.5z" fill="#29a8e0"/></svg>
        7(955)482-3170
        <svg width="12" height="8" viewBox="0 0 12 8"><rect width="12" height="2.7" fill="#fff" stroke="#ddd" stroke-width=".3"/><rect y="2.7" width="12" height="2.7" fill="#0039a6"/><rect y="5.3" width="12" height="2.7" fill="#d52b1e"/></svg>
      </p>
      <p class="contact">
        <svg width="8" height="6" viewBox="0 0 10 7"><rect width="10" height="7" fill="#29a8e0"/><path d="M0 0l5 4 5-4" stroke="#fff" fill="none"/></svg>
        melnovetz@quorbamail.com
      </p>
      <p class="contact">
        <svg width="8" height="8" viewBox="0 0 10 10"><circle cx="5" cy="5" r="5" fill="#29a8e0"/></svg>
        boris_m
      </p>
      <p class="social"><span class="social__box"></span><span class="social__box"></span><span class="social__handle">/melnovetz</span></p>
    </div>
    <div class="base-rule base-rule--grey"></div>
    <div class="base-rule base-rule--blue"></div>
  </section>
  <span class="side-label" style="top:795px">Back 2</span>

</main>
</body>
</html>
```